Web site for a company that sells Pinball machines

We need a website that is an online shopping experience for a Store that sells pinball machines and accessories. The name of the store is called "Bumper Vault Arcade." The store it self has a showroom, but we would also like to have an Internet e-commerce presence. We pinball machines made by Halvern gameworks. You can visit their website and see their current list of machines as well as their website for the machines that we are going to carry in our store. Their website is Halverngameworks.example. I am able to use their machine photos as well as their machine brochure PDF files. I am also able to use their logo on my website two list it as a Halvern Authorized Dealer.
This website design needs to be funky, fun, very technologically oriented and modern. The people buying machines our spending anywhere between $5000 and $15,000 on one machine. These Are high-end buyers who are also usually fairly tech savvy or at least enjoy technology and graphics.
Attachments: I have attached photographs of some of my own machines which may be used in the website. I've also attached some downloaded files from Halvern gameworks.example as well as some of their PDF files for brochures. I will carry all of their current models they have listed under games. Not the archived games. I have included one of their machines called Copperfield Limited edition in my photograph attachments. The rest of the photos are just random pictures that I have taken myself and maybe used to build the site. Lastly I have attached my logo which I am not super crazy about so I will also be posting a contest to redesign this logo. Tons more of my own pinball photos are available.
I would like for people to be able to purchase machines and accessories from the website, but also inform them to our actual showroom.
Updates
Target Market(s)
Target market is 16 to 75. Techy individuals to enjoy gaming technology video animation and Vegas style twinkle
Industry/Entity Type
It Company
Coding
Coded - Design and coding required
Number of Pages Required
3 page
Look and feel

```html
<!DOCTYPE html>
<html lang="en">
<head>
<meta charset="utf-8">
<title>Bumper Vault Arcade</title>
<link rel="stylesheet" href="https://fonts.googleapis.com/css2?family=Open+Sans:wght@400;600;700;800&display=swap">
<style>
:root{
  --gold:#c8b95b;
  --gold-dark:#b5a548;
  --ink:#333;
  --muted:#777;
  --page:#ececec;
  --white:#fff;
  --sky:#d6ebf5;
  --blush:#eee2e8;
  --photo-warm:linear-gradient(135deg,#6b2a12 0%,#d98a1f 35%,#f2c43a 55%,#b8261c 75%,#3a1a10 100%);
  --photo-cool:linear-gradient(135deg,#1b2340 0%,#3b4f8a 40%,#c2402a 70%,#e8b23a 100%);
}
*{box-sizing:border-box;margin:0;padding:0}
html,body{width:1200px;height:5018px;overflow:hidden}
body{position:relative;background:var(--page);font-family:"Open Sans",Arial,sans-serif;color:var(--ink)}
.abs{position:absolute}
.photo{position:absolute;background:var(--photo-warm)}
.photo.cool{background:var(--photo-cool)}
.btn{position:absolute;background:var(--gold);color:var(--white);border-radius:20px;font-size:13px;font-weight:600;display:flex;align-items:center;justify-content:center}
.gold-head{position:absolute;color:var(--gold);font-weight:700;font-size:24px;text-transform:uppercase}
.copy{position:absolute;font-size:13px;line-height:1.55;color:var(--muted)}

/* header */
.site-header{position:absolute;left:0;top:0;width:1200px;height:94px;background:var(--white)}
.brand{position:absolute;left:70px;top:28px;display:flex;align-items:center;gap:10px;font-size:18px;font-weight:700;color:var(--ink)}
.brand-dot{width:34px;height:34px;border-radius:50%;background:var(--gold)}
.nav a{position:absolute;top:0;height:94px;display:flex;align-items:center;justify-content:center;font-size:14px;font-weight:600;color:var(--ink);text-decoration:none}
.nav a.active{background:var(--gold);color:var(--white)}
.search{position:absolute;left:1039px;top:30px;width:134px;height:34px;border-radius:17px;background:#f2f2f2;border:1px solid #e2e2e2;font-size:13px;color:#aaa;padding:8px 16px}

/* hero */
.hero{position:absolute;left:0;top:94px;width:1200px;height:593px;background:var(--photo-warm)}
.hero-strip{position:absolute;left:0;top:459px;width:1200px;height:134px;background:rgba(20,10,5,.75)}
.hero-thumb{position:absolute;top:476px;width:168px;height:77px;border:3px solid var(--white);background:var(--photo-cool)}
.hero-panel{position:absolute;left:60px;top:13px;width:369px;height:362px;background:rgba(255,255,255,.82);padding:24px 32px}
.hero-panel .kicker{font-size:14px;font-weight:700}
.hero-panel h1{font-size:56px;line-height:1.05;font-weight:800;margin:22px 0 14px;text-transform:uppercase}
.hero-panel p{font-size:13px;line-height:1.5}

/* sections */
.card{position:absolute;background:var(--white)}
.tag{position:absolute;top:2273px;width:104px;height:37px;background:var(--gold);color:var(--white);font-size:12px;font-weight:600;display:flex;align-items:center;justify-content:center;text-transform:uppercase}
.product{position:absolute;top:2457px;width:195px;height:503px;background:var(--white);box-shadow:0 2px 6px rgba(0,0,0,.12)}
.product .shot{position:absolute;left:0;top:0;width:195px;height:285px;background:var(--photo-cool)}
.product .info{position:absolute;left:12px;top:300px;font-size:13px;line-height:1.5;color:var(--muted)}
.product .info b{display:block;color:var(--ink);font-weight:700;text-transform:uppercase}
.arrow{position:absolute;top:2571px;width:34px;height:77px;background:var(--gold);display:flex;align-items:center;justify-content:center}

/* contact */
.field{position:absolute;left:248px;width:687px;background:var(--white);border:1px solid #e0d6db;font-size:13px;color:#999;padding:10px 14px}

/* footer */
.site-footer{position:absolute;left:0;top:4549px;width:1200px;height:469px;background:var(--gold);color:var(--white);text-align:center}
.site-footer .line{position:absolute;left:0;width:1200px;font-size:13px}
.social{position:absolute;top:4854px;width:60px;height:60px;border-radius:50%;border:2px solid var(--white)}
</style>
</head>
<body>

<header class="site-header">
  <div class="brand"><span class="brand-dot"></span>Bumper Vault Arcade</div>
  <nav class="nav">
    <a class="active" href="#" style="left:452px;width:101px">HOME</a>
    <a href="#" style="left:585px;width:76px">ABOUT US</a>
    <a href="#" style="left:700px;width:76px">PRODUCTS</a>
    <a href="#" style="left:820px;width:62px">SHOP</a>
    <a href="#" style="left:920px;width:90px">CONTACT US</a>
  </nav>
  <div class="search">Search</div>
</header>

<section class="hero" role="img" aria-label="Close-up photo of a pinball playfield with a red dome light">
  <div class="hero-panel">
    <div class="kicker">Lorem ipsum dolor</div>
    <h1>Lorem<br>Ipsum</h1>
    <p>Lorem ipsum dolor sit amet, consectetuer adipiscing elit. Aenean commodo ligula eget dolor. Aenean massa. Cum sociis natoque penatibus et magnis dis parturient montes, nascetur ridiculus mus. Donec quam felis, ultricies nec.</p>
    <div class="btn" style="left:32px;top:292px;width:102px;height:26px;font-size:11px">Read more ›</div>
  </div>
  <div class="hero-strip"></div>
  <div class="hero-thumb" style="left:127px" role="img" aria-label="Pinball machine thumbnail"></div>
  <div class="hero-thumb" style="left:318px" role="img" aria-label="Pinball machine thumbnail"></div>
  <div class="hero-thumb" style="left:513px" role="img" aria-label="Pinball machine thumbnail"></div>
  <div class="hero-thumb" style="left:707px" role="img" aria-label="Pinball machine thumbnail"></div>
  <div class="hero-thumb" style="left:898px" role="img" aria-label="Pinball machine thumbnail"></div>
</section>

<!-- welcome -->
<section class="card" style="left:50px;top:715px;width:1100px;height:520px"></section>
<div class="photo" style="left:60px;top:731px;width:336px;height:409px" role="img" aria-label="Pinball playfield photo"></div>
<h2 class="gold-head" style="left:600px;top:745px;width:523px;text-align:right">Welcome to lorem ipsum</h2>
<p class="copy" style="left:430px;top:791px;width:693px;text-align:right">Aliquam sit amet neque sapien, a ornare felis. Fusce sollicitudin velit at eleifend laoreet, dui turpis pulvinar justo, eget sagittis arcu ipsum eu est. Praesentaliquam tincidunt accumsan sodales. Vivamus eros tempus, egestas ullamcorper magna at, elementum ipsum dolor mauris cursus eget.<br><br>Praesent vitae leo magna, sed dignissim eros. Class aptent taciti sociosqu ad litora torquent per conubia nostra, per inceptos himenaeos. Sed ultrices fermentum dictum. Nullam nec elit magnis et malesuada massa.</p>
<div class="btn" style="left:999px;top:966px;width:117px;height:36px">Read more ›</div>
<div class="photo cool" style="left:426px;top:1046px;width:217px;height:177px" role="img" aria-label="Pinball detail photo"></div>
<div class="photo cool" style="left:667px;top:1046px;width:218px;height:177px" role="img" aria-label="Pinball detail photo"></div>
<div class="photo cool" style="left:908px;top:1046px;width:218px;height:177px" role="img" aria-label="Pinball detail photo"></div>

<section class="card" style="left:50px;top:1235px;width:1100px;height:1110px"></section>
<h2 class="gold-head" style="left:60px;top:1248px">Welcome to lorem ipsum</h2>
<p class="copy" style="left:60px;top:1290px;width:780px">Aliquam sit amet neque sapien, a ornare felis. Fusce sollicitudin velit at eleifend laoreet, dui turpis pulvinar justo, eget sagittis arcu ipsum eu est. Praesentaliquam tincidunt accumsan sodales. Vivamus posuere aliquam adipiscing. Aenean dictum ipsum et mauris cursus eget bibendum purus condimentum. Mauris sapien nunc aliquet vitae dapibus nec, ultricies vel est. Vivamus eros tempus.<br><br>Praesent vitae leo magna, sed dignissim eros. Class aptent taciti sociosqu ad litora torquent per conubia nostra, per inceptos himenaeos. Sed ultrices fermentum dictum. Nullam nec elit magnis et malesuada massa. Cum sociis natoque penatibus et magnis dis parturient montes, nascetur ridiculus mus.</p>
<div class="btn" style="left:70px;top:1505px;width:117px;height:36px">Read more ›</div>
<div class="photo cool" style="left:878px;top:1264px;width:245px;height:502px" role="img" aria-label="Pinball backglass artwork photo"></div>
<div class="photo" style="left:60px;top:1582px;width:791px;height:184px" role="img" aria-label="Row of pinball machines in a showroom"></div>
<h2 class="gold-head" style="left:0;top:1782px;width:1200px;text-align:center">Welcome to lorem ipsum</h2>
<div class="photo" style="left:60px;top:1887px;width:1063px;height:366px" role="img" aria-label="Pinball playfield with red dome light"></div>
<div class="tag" style="left:154px">Lorem ipsum</div>
<div class="tag" style="left:264px">Lorem ipsum</div>
<div class="tag" style="left:374px">Lorem ipsum</div>
<div class="tag" style="left:484px">Lorem ipsum</div>
<div class="tag" style="left:594px">Lorem ipsum</div>
<div class="tag" style="left:704px">Lorem ipsum</div>
<div class="tag" style="left:814px">Lorem ipsum</div>
<div class="tag" style="left:924px">Lorem ipsum</div>

<!-- products -->
<section class="abs" style="left:0;top:2390px;width:1200px;height:855px;background:var(--sky)"></section>
<section class="card" style="left:50px;top:2390px;width:1090px;height:778px;border-bottom:4px solid var(--gold)"></section>
<h2 class="gold-head" style="left:0;top:2408px;width:1200px;text-align:center">Lorem ipsum</h2>
<div class="arrow" style="left:77px"><svg width="12" height="18" viewBox="0 0 12 18"><path d="M10 2 3 9l7 7" stroke="#fff" stroke-width="3" fill="none"/></svg></div>
<div class="arrow" style="left:1049px"><svg width="12" height="18" viewBox="0 0 12 18"><path d="M2 2l7 7-7 7" stroke="#fff" stroke-width="3" fill="none"/></svg></div>
<div class="product" style="left:168px"><div class="shot" role="img" aria-label="Pinball machine product photo"></div><div class="info"><b>Lorem<br>ipsum</b>Pellentesque<br>eget erat<br>at libero<br>folia orci<br>feugiat<br>malesuada<br>etud...</div></div>
<div class="product" style="left:389px"><div class="shot" role="img" aria-label="Pinball machine product photo"></div><div class="info"><b>Lorem<br>ipsum</b>Pellentesque<br>eget erat<br>at libero<br>folia orci<br>feugiat<br>malesuada<br>etud...</div></div>
<div class="product" style="left:610px"><div class="shot" role="img" aria-label="Pinball machine product photo"></div><div class="info"><b>Lorem<br>ipsum</b>Pellentesque<br>eget erat<br>at libero<br>folia orci<br>feugiat<br>malesuada<br>etud...</div></div>
<div class="product" style="left:831px"><div class="shot" role="img" aria-label="Pinball machine product photo"></div><div class="info"><b>Lorem<br>ipsum</b>Pellentesque<br>eget erat<br>at libero<br>folia orci<br>feugiat<br>malesuada<br>etud...</div></div>
<div class="btn" style="left:449px;top:3020px;width:285px;height:74px;border-radius:37px;font-size:24px;font-weight:700;gap:10px">
  <svg width="22" height="22" viewBox="0 0 22 22"><rect x="2" y="5" width="15" height="15" fill="none" stroke="#fff" stroke-width="2.5"/><path d="M9 13 19 3" stroke="#fff" stroke-width="3"/></svg>LOREM IPSUM</div>

<!-- feature photo -->
<section class="photo" style="left:0;top:3245px;width:1200px;height:670px" role="img" aria-label="Large close-up photo of a pinball playfield"></section>
<div class="card" style="left:60px;top:3362px;width:610px;height:392px;padding:55px 60px">
  <h2 style="font-size:28px;font-weight:700;margin-bottom:24px">LOREM IPSUM</h2>
  <p style="font-size:13px;line-height:1.55;color:var(--muted)">Sed ultricies fermentum dictum. Nullam nec elit magnis, at malesuada massa. Cum sociis natoque penatibus et magnis dis parturient montes, nascetur ridiculus mus. Donec id orci mi. Phasellus quam metus, condimentum tempus sed blandit at, laoreet et nulla. Curabitur dui arcu, adipiscing ut semper vitae, tincidunt vel nisl.<br><br>Aliquam sit amet neque sapien, a ornare felis. Fusce sollicitudin, velit at eleifend laoreet, dui turpis pulvinar justo, eget sagittis arcu ipsum eu est. Praesentaliquam tincidunt accumsan sodales. Etiam posuere aliquam adipiscing. Aenean dictum ipsum et mauris cursus eget bibendum purus condimentum. Mauris sapien nunc, aliquet vitae dapibus nec, ultricies vel est.</p>
</div>

<!-- contact -->
<section class="abs" style="left:0;top:3915px;width:1200px;height:634px;background:var(--blush)"></section>
<h2 class="gold-head" style="left:0;top:3987px;width:1200px;text-align:center;font-size:22px">Contact us</h2>
<div class="field" style="top:4076px;height:44px">Name</div>
<div class="field" style="top:4150px;height:43px">Email</div>
<div class="field" style="top:4217px;height:43px">Subject</div>
<div class="field" style="top:4284px;height:121px">Message</div>
<div class="btn" style="left:513px;top:4431px;width:161px;height:44px;border-radius:10px">Lorem ipsum</div>

<!-- footer -->
<footer class="site-footer">
  <svg class="abs" style="left:570px;top:80px" width="60" height="54" viewBox="0 0 60 54"><path d="M30 2 2 28h8v24h16V36h8v16h16V28h8z" fill="#fff"/></svg>
  <div class="line" style="top:162px">Phasellus ipsum, Lorem ipsum, Lorem ipsum</div>
  <div class="line" style="top:196px">Tel: 000000000, Fax: 000000000, Mobile: 000000000, 000000000</div>
  <div class="line" style="top:236px">email: hello@bumpervault.example</div>
  <div class="social" style="left:466px;top:305px"></div>
  <div class="social" style="left:533px;top:305px"></div>
  <div class="social" style="left:600px;top:305px"></div>
  <div class="social" style="left:667px;top:305px"></div>
  <div class="line" style="top:404px;font-size:12px">© Copyright Lorem Ipsum 2015 All Right Reserved</div>
</footer>

</body>
</html>
```